Commercial construction contractor website.

We need a website that contains About Us, Contact info, Services, Project pictures and Industry News section

Target Market(s)

I'm building industral/flex spaces/commercial.

Industry/Entity Type

Commercial/industrial construction

Coding

Coded - Design and coding required

Number of Pages Required

5+ page

Font styles to use
Other font styles liked:
• The logo font is Microgramma Pro

Requirements
Must have
• Must have correct company name spelling: Halvern Ridge Construction
Nice to have
• I do like to see our logo design implemented in the design
Should not have
• Please do not show big city pictures and business suit people. We are a commercial construction company

```html
<!DOCTYPE html>
<html lang="en">
<head>
<meta charset="utf-8">
<title>Halvern Ridge Construction</title>
<link rel="stylesheet" href="https://fonts.googleapis.com/css2?family=Michroma&family=Montserrat:wght@400;500;600;700;800&display=swap">
<style>
:root{
  --blue:#1573c4;
  --blue-dark:#0d4f8f;
  --navy:#0e1a2b;
  --ink:#1d232c;
  --text:#4f5560;
  --muted:#8a9099;
  --line:#e3e6ea;
  --white:#ffffff;
  --grey-btn:#55595f;
  --head:"Michroma",sans-serif;
  --body:"Montserrat",sans-serif;
}
*{box-sizing:border-box;margin:0;padding:0}
html,body{width:1200px;height:3544px;overflow:hidden}
body{position:relative;background:var(--white);font-family:var(--body);color:var(--text)}
.abs{position:absolute}
.ph{position:absolute}

/* Header / hero */
.hero{left:0;top:0;width:1200px;height:620px;background:linear-gradient(160deg,#4b5159 0%,#2f343b 45%,#1c2027 100%)}
.hero-shade{left:0;top:0;width:1200px;height:620px;background:linear-gradient(180deg,rgba(10,14,20,.35),rgba(10,14,20,.55))}
.logo-box{left:80px;top:0;width:230px;height:138px;background:var(--white);border-bottom:8px solid var(--blue);display:flex;flex-direction:column;align-items:center;justify-content:center;gap:10px}
.logo-mark{width:40px;height:40px;border-radius:50%;background:var(--blue)}
.logo-name{font-family:var(--body);font-weight:700;font-size:14px;color:var(--blue-dark);text-transform:uppercase;text-align:center;line-height:1.3;letter-spacing:.5px}
.nav{left:446px;top:38px;display:flex;gap:24px}
.nav a{font-family:var(--body);font-weight:600;font-size:12px;color:var(--white);text-decoration:none;padding-bottom:8px;white-space:nowrap}
.nav a.active{color:#6fb6ff;border-bottom:3px solid var(--blue)}
.quote-btn{left:976px;top:24px;width:130px;height:42px;background:var(--grey-btn);color:var(--white);font-weight:700;font-size:12px;display:flex;align-items:center;justify-content:center;letter-spacing:.5px}
.hero-title{left:0;top:272px;width:1200px;text-align:center;font-family:var(--head);font-size:46px;line-height:60px;color:var(--white)}
.call-box{left:800px;top:498px;width:400px;height:86px;background:var(--blue);display:flex;align-items:center;gap:18px;padding-left:34px;color:var(--white)}
.call-box small{display:block;font-size:12px;font-weight:600;letter-spacing:1px}
.call-box strong{display:block;font-family:var(--head);font-size:24px;margin-top:4px}

/* About */
.about-card{left:96px;top:586px;width:1010px;height:500px;background:var(--white);box-shadow:10px 10px 0 var(--blue),0 10px 30px rgba(0,0,0,.12)}
.about-photo{left:130px;top:618px;width:400px;height:440px;background:linear-gradient(150deg,#e7eaee,#b9c6d3 60%,#8ea4b9)}
.year-badge{left:452px;top:850px;width:92px;height:100px;background:var(--blue);border:4px solid var(--white);color:var(--white);text-align:center;padding-top:12px}
.year-badge b{display:block;font-family:var(--head);font-size:30px}
.year-badge span{font-size:14px;font-weight:600}
.about-body{left:614px;top:650px;width:440px}
.sec-title{font-family:var(--head);font-size:34px;color:var(--blue);text-transform:uppercase}
.about-body .lead{margin-top:20px;font-weight:700;font-size:16px;color:var(--ink);line-height:1.5}
.about-body p{margin-top:14px;font-size:12px;line-height:1.7}
.dark-btn{display:inline-flex;align-items:center;justify-content:center;width:120px;height:36px;background:var(--grey-btn);color:var(--white);font-size:11px;font-weight:700;letter-spacing:.5px}

/* Services */
.services{left:0;top:1140px;width:1200px;height:580px;background:linear-gradient(120deg,#1b5fa8 0%,#2b4f7e 40%,#1a2535 100%)}
.services-shade{left:0;top:1140px;width:1200px;height:580px;background:linear-gradient(90deg,rgba(20,90,170,.55),rgba(12,18,28,.7))}
.services-title{left:120px;top:1296px;font-family:var(--head);font-size:32px;color:var(--white)}
.svc{top:1352px;width:300px;height:244px;background:var(--white);padding:28px 24px}
.svc svg{display:block}
.svc h3{margin-top:14px;font-family:var(--body);font-weight:800;font-size:19px;line-height:1.25;color:var(--blue-dark);text-transform:uppercase}
.svc p{margin-top:12px;font-size:11px;line-height:1.6}
.svc.active{background:var(--blue)}
.svc.active h3,.svc.active p{color:var(--white)}
.svc-nav{left:238px;top:1624px;display:flex;align-items:center;gap:8px;color:var(--white);font-size:13px;font-weight:600}
.arrow-sq{width:28px;height:28px;border:1px solid rgba(255,255,255,.6);display:flex;align-items:center;justify-content:center}

/* Projects */
.projects-title{left:0;top:1812px;width:1200px;text-align:center;font-family:var(--head);font-size:32px;color:var(--blue)}
.proj{width:324px;box-shadow:0 6px 18px rgba(0,0,0,.08)}
.proj .img{height:236px}
.proj .cap{height:72px;background:var(--white);padding:16px 20px}
.proj .cap b{display:block;font-weight:700;font-size:14px;color:var(--ink);text-transform:uppercase}
.proj .cap span{display:block;margin-top:6px;font-size:11px;color:var(--muted)}
.proj.active .cap{background:var(--blue)}
.proj.active .cap b,.proj.active .cap span{color:var(--white)}
.blue-btn{display:flex;align-items:center;justify-content:center;background:var(--blue);color:var(--white);font-size:12px;font-weight:700;letter-spacing:.5px}

/* News */
.news-band{left:40px;top:2748px;width:1160px;height:432px;background:linear-gradient(90deg,#3a4048 0%,#232830 100%)}
.news-title{left:88px;top:2690px;font-family:var(--head);font-size:32px;color:var(--blue)}
.news-card{left:88px;top:2764px;width:610px;height:256px;background:var(--white);padding:26px 30px;box-shadow:0 8px 24px rgba(0,0,0,.18)}
.news-card h3{font-weight:700;font-size:16px;line-height:1.4;color:var(--blue-dark);text-transform:uppercase;width:460px}
.news-card p{margin-top:14px;font-size:12px;line-height:1.65;width:470px}
.news-meta{margin-top:20px;display:flex;align-items:center;gap:14px;font-size:11px;color:var(--muted)}
.news-photo{left:620px;top:2728px;width:472px;height:380px;background:linear-gradient(160deg,#b7cde2,#6f8fae 50%,#5f7b4c 100%)}
.mini{top:3060px;display:flex;gap:12px;align-items:center}
.mini .thumb{width:68px;height:52px;flex:none}
.mini b{display:block;font-size:12px;font-weight:700;color:var(--white);line-height:1.35;width:130px}
.mini span{display:block;margin-top:4px;font-size:10px;color:#c9ced5}

/* Footer */
.footer{left:0;top:3180px;width:1200px;height:320px;background:var(--navy)}
.f-logo{left:110px;top:3236px;width:200px;display:flex;flex-direction:column;align-items:center;gap:14px}
.f-logo .logo-name{color:var(--white)}
.f-col{top:3210px}
.f-col h4{font-size:13px;font-weight:700;color:#6fb6ff;text-transform:uppercase;margin-bottom:18px}
.f-row{display:flex;gap:12px;align-items:flex-start;font-size:12px;color:#d3d8df;line-height:1.5;margin-bottom:14px}
.f-links a{display:block;font-size:12px;color:#d3d8df;text-decoration:none;margin-bottom:12px}
.map{left:868px;top:3222px;width:244px;height:176px;background:linear-gradient(135deg,#e8ece6,#cfd8c8)}
.copy{left:0;top:3500px;width:1200px;height:44px;background:var(--blue);display:flex;align-items:center;justify-content:space-between;padding:0 88px;color:var(--white);font-size:11px}
.social{display:flex;gap:12px}
.social i{width:12px;height:12px;border-radius:50%;background:var(--white);display:block}
</style>
</head>
<body>

<!-- Header and hero -->
<div class="ph hero" role="img" aria-label="Construction workers in hard hats and safety vests at a building site"></div>
<div class="ph hero-shade"></div>
<div class="abs logo-box">
  <div class="logo-mark"></div>
  <div class="logo-name">Halvern Ridge<br>Construction</div>
</div>
<nav class="abs nav">
  <a class="active" href="#">HOME</a>
  <a href="#">ABOUT US</a>
  <a href="#">SERVICES</a>
  <a href="#">PROJECTS</a>
  <a href="#">NEWS</a>
  <a href="#">CONTACT US</a>
</nav>
<div class="abs quote-btn">GET A QUOTE</div>
<h1 class="abs hero-title">We Build Your<br>Dream with Passion</h1>
<div class="abs call-box">
  <svg width="34" height="34" viewBox="0 0 24 24" fill="none" stroke="#fff" stroke-width="1.8"><path d="M5 3h4l2 5-2.5 1.5a11 11 0 0 0 6 6L16 13l5 2v4a2 2 0 0 1-2 2A16 16 0 0 1 3 5a2 2 0 0 1 2-2z"/></svg>
  <div><small>CALL TODAY</small><strong>(555) 304-7182</strong></div>
</div>

<!-- About -->
<div class="abs about-card"></div>
<div class="ph about-photo" role="img" aria-label="Smiling builder in a yellow hard hat giving a thumbs up"></div>
<div class="abs year-badge"><b>20</b><span>Year</span></div>
<div class="abs about-body">
  <h2 class="sec-title">About Us</h2>
  <div class="lead">Lorem Ipsum is simply dummy text of the printing and typesetting industry.</div>
  <p>Lorem Ipsum has been the industry's standard dummy text ever since the 1500s, when an unknown printer took a galley of type and scrambled it to make a type specimen book.</p>
  <p>It has survived not only five centuries, but also the leap into electronic typesetting, remaining essentially unchanged.</p>
  <div style="margin-top:22px"><span class="dark-btn">READ MORE</span></div>
</div>

<!-- Services -->
<div class="ph services" role="img" aria-label="Builder on a site with scaffolding, tinted blue"></div>
<div class="ph services-shade"></div>
<h2 class="abs services-title">SERVICES WE PROVIDE</h2>
<div class="abs svc" style="left:120px">
  <svg width="42" height="42" viewBox="0 0 42 42" fill="none" stroke="#0d4f8f" stroke-width="2"><path d="M8 26a13 13 0 0 1 26 0"/><path d="M5 26h32v4H5z"/><path d="M21 13v6M16 15l1 5M26 15l-1 5"/><path d="M12 34h18v4H12z"/></svg>
  <h3>Construction<br>Services</h3>
  <p>Lorem Ipsum is simply dummy text of the printing and typesetting industry. Lorem Ipsum.</p>
</div>
<div class="abs svc" style="left:448px">
  <svg width="42" height="42" viewBox="0 0 42 42" fill="none" stroke="#0d4f8f" stroke-width="2"><path d="M6 38V18l15-10 15 10v20z"/><path d="M14 38V26h14v12"/><path d="M14 20h14"/></svg>
  <h3>Design &amp;<br>Estimating</h3>
  <p>Lorem Ipsum is simply dummy text of the printing and typesetting industry. Lorem Ipsum.</p>
</div>
<div class="abs svc active" style="left:772px">
  <svg width="42" height="42" viewBox="0 0 42 42" fill="none" stroke="#fff" stroke-width="2"><path d="M3 18h36M3 30h36"/><path d="M8 18v18M34 18v18M14 18v12M21 18v12M28 18v12"/><path d="M8 18V8M34 18V8M8 10l13 8 13-8"/></svg>
  <h3>Bridge<br>Construction</h3>
  <p>Lorem Ipsum is simply dummy text of the printing and typesetting industry. Lorem Ipsum.</p>
</div>
<div class="abs svc-nav">
  <span class="arrow-sq"><svg width="10" height="10" viewBox="0 0 10 10"><path d="M7 1 3 5l4 4" stroke="#fff" fill="none" stroke-width="1.5"/></svg></span>
  <span class="arrow-sq"><svg width="10" height="10" viewBox="0 0 10 10"><path d="M3 1l4 4-4 4" stroke="#fff" fill="none" stroke-width="1.5"/></svg></span>
  <span>View All</span>
</div>

<!-- Projects -->
<h2 class="abs projects-title">PROJECTS</h2>
<div class="abs proj" style="left:88px;top:1888px">
  <div class="img" style="background:linear-gradient(160deg,#dfe6ee,#9aa8b6)" role="img" aria-label="Concrete building frame under construction"></div>
  <div class="cap"><b>Interior Texture</b><span>Buildings, Interior</span></div>
</div>
<div class="abs proj active" style="left:440px;top:1888px">
  <div class="img" style="background:linear-gradient(160deg,#8b6a3d,#d3a24a 50%,#5c4a36)" role="img" aria-label="Workers in orange gear on steel formwork"></div>
  <div class="cap"><b>Bengit Architecture</b><span>Buildings, Interior</span></div>
</div>
<div class="abs proj" style="left:788px;top:1888px">
  <div class="img" style="background:linear-gradient(160deg,#c9d8e6,#b48a55 55%,#6b5a48)" role="img" aria-label="Modern villa with timber facade at sunset"></div>
  <div class="cap"><b>Contemporary Villa</b><span>Buildings, Interior</span></div>
</div>
<div class="abs proj" style="left:88px;top:2212px">
  <div class="img" style="background:linear-gradient(160deg,#f1f3f5,#a7b3bf 60%,#c6a33a)" role="img" aria-label="Worker standing beneath a steel structure frame"></div>
  <div class="cap"><b>Interior Texture</b><span>Buildings, Interior</span></div>
</div>
<div class="abs proj" style="left:440px;top:2212px">
  <div class="img" style="background:linear-gradient(170deg,#c7d1da,#8c8f93 55%,#b3332c)" role="img" aria-label="Road roller compacting fresh asphalt"></div>
  <div class="cap"><b>Bengit Architecture</b><span>Buildings, Interior</span></div>
</div>
<div class="abs proj" style="left:788px;top:2212px">
  <div class="img" style="background:linear-gradient(160deg,#8fb7e0,#e9eef3 50%,#2f5d9c)" role="img" aria-label="Blue and white industrial warehouse building"></div>
  <div class="cap"><b>Contemporary Villa</b><span>Buildings, Interior</span></div>
</div>
<div class="abs blue-btn" style="left:546px;top:2552px;width:108px;height:34px">VIEW ALL</div>

<!-- News -->
<div class="ph news-band" role="img" aria-label="Dark construction site backdrop"></div>
<h2 class="abs news-title">LATEST NEWS</h2>
<div class="ph news-photo" role="img" aria-label="Modern glass office building with trees"></div>
<div class="abs news-card">
  <h3>Lorem Ipsum is simply dummy text of the printing and typesetting industry</h3>
  <p>Lorem Ipsum is simply dummy text of the printing and typesetting industry. Lorem Ipsum has been the industry's standard dummy text ever since the 1500s, when an unknown printer took a galley of type and scrambled it to make a type specimen book. It has survived not only five centuries, but also the leap into electronic.</p>
  <div class="news-meta">
    <svg width="16" height="16" viewBox="0 0 16 16" fill="none" stroke="#1573c4" stroke-width="1.4"><rect x="2" y="3" width="12" height="11"/><path d="M2 6h12M5 1v3M11 1v3"/></svg>
    <span>05 Jan 2020</span>
    <span class="blue-btn" style="width:96px;height:30px;margin-left:16px">READ MORE</span>
    <span style="margin-left:auto;display:flex;gap:6px">
      <span class="arrow-sq" style="border-color:#c5cad0"><svg width="10" height="10" viewBox="0 0 10 10"><path d="M7 1 3 5l4 4" stroke="#8a9099" fill="none" stroke-width="1.5"/></svg></span>
      <span class="arrow-sq" style="border-color:#1573c4;background:#1573c4"><svg width="10" height="10" viewBox="0 0 10 10"><path d="M3 1l4 4-4 4" stroke="#fff" fill="none" stroke-width="1.5"/></svg></span>
    </span>
  </div>
</div>
<div class="abs mini" style="left:88px">
  <div class="thumb" style="background:linear-gradient(160deg,#d7a64b,#6b5a48)" role="img" aria-label="Workers on a building site"></div>
  <div><b>Lorem Ipsum is simply dummy text</b><span>05 Jan 2020</span></div>
</div>
<div class="abs mini" style="left:348px">
  <div class="thumb" style="background:linear-gradient(160deg,#c7d1da,#b3332c)" role="img" aria-label="Road works with heavy machinery"></div>
  <div><b>Lorem Ipsum is simply dummy text</b><span>05 Jan 2020</span></div>
</div>

<!-- Footer -->
<div class="abs footer"></div>
<div class="abs f-logo">
  <div class="logo-mark" style="width:56px;height:56px"></div>
  <div class="logo-name">Halvern Ridge<br>Construction</div>
</div>
<div class="abs f-col" style="left:356px;width:230px">
  <h4>Contact Info</h4>
  <div class="f-row"><svg width="14" height="14" viewBox="0 0 24 24" fill="#6fb6ff"><path d="M12 2a7 7 0 0 0-7 7c0 5 7 13 7 13s7-8 7-13a7 7 0 0 0-7-7zm0 9.5A2.5 2.5 0 1 1 12 6.5a2.5 2.5 0 0 1 0 5z"/></svg><span>12 Quarry Lane,<br>Eastfield 4021</span></div>
  <div class="f-row"><svg width="14" height="14" viewBox="0 0 24 24" fill="#6fb6ff"><path d="M5 3h4l2 5-2.5 1.5a11 11 0 0 0 6 6L16 13l5 2v4a2 2 0 0 1-2 2A16 16 0 0 1 3 5a2 2 0 0 1 2-2z"/></svg><span>+1 555 304 7190</span></div>
  <div class="f-row"><svg width="14" height="14" viewBox="0 0 24 24" fill="none" stroke="#6fb6ff" stroke-width="2"><rect x="2" y="5" width="20" height="14"/><path d="M2 6l10 7 10-7"/></svg><span>info@halvernridge.com</span></div>
</div>
<div class="abs f-col f-links" style="left:616px;width:110px">
  <h4>Quick Link</h4>
  <a href="#">Home</a><a href="#">About Us</a><a href="#">Services</a><a href="#">Projects</a>
</div>
<div class="abs f-col f-links" style="left:736px;top:3246px;width:100px">
  <a href="#">News</a><a href="#">Contact Us</a>
</div>
<div class="ph map" role="img" aria-label="Location map of the office"></div>
<div class="abs copy">
  <span>Copyright © 2020 Halvern Ridge. All Rights Reserved</span>
  <span class="social"><i></i><i></i><i></i></span>
</div>

</body>
</html>
```